Business Card Design Project

I am looking for a minimal matte background/shiny (spot UV) ink monochromatic design with a splash of neon color.

the card should be 2 sided, logo only on one side - all info and possibly logo on the other.

My creative director described the colors he imagined for the design to be:
'it's a dark field, like charcoal or a really dark burgundy, or deep blue, shot through with a neon—but just a tiny bit of it. so a charcoal field with a laser-thin streak of electric lime, safety orange, or cobalt blue. really beautiful stuff.'

here are some samples of the types of cards I am trying to create:
http://www.pictavault.example/photos/dawnpress/6967376935/in/photostream -> Vandrelle Lustre

http://www.pictavault.example/photos/dawnpress/6497659409/in/photostream -> Standard Coated (14pt/matte) with SPOT UV

http://www.pictavault.example/photos/dawnpress/6497658995/in/photostream/ -> Heavy Corvane with Raised Ink

http://www.pictavault.example/photos/dawnpress/6275629165/in/photostream/ -> Standard Coated (14pt/matte) with SPOT UV

Here is my logo:
https://www.filecrate.example/s/sigym192mlh58ge/quillorb%20logotype%20final.ai

Here are the details for info:
Dorian Elwood Marsh
email - dorian@quillorb.example
mobile - 555 013 2867
web -
quillorb.example: inventive technology applications
quillorb-tv.example: innovative video advertising

please let me know if there is anything at all that you need.

Target Market(s)

mid to large agencies that require interactive design and entrepreneurial/startup individuals/companies that need application development.

Industry/Entity Type

Safety

Requirements
Must have
• logo only on one side

```html
<!DOCTYPE html>
<html lang="en">
<head>
<meta charset="utf-8">
<title>Quillorb business card</title>
<link rel="stylesheet" href="https://fonts.googleapis.com/css2?family=Bebas+Neue&family=Open+Sans:wght@400;700&display=swap">
<style>
  :root {
    --field: #1f1f22;
    --field-edge: #18181a;
    --paper: #ffffff;
    --neon: #ff6a00;
    --neon-soft: rgba(255, 106, 0, 0.35);
    --wordmark-faint: #3a3a3e;
    --text: #d9d9dc;
    --disc-core: #2c2c30;
    --disc-edge: #222225;
  }
  * { margin: 0; padding: 0; box-sizing: border-box; }
  html, body { width: 1200px; height: 1042px; overflow: hidden; background: var(--paper); }
  .sheet { position: relative; width: 1200px; height: 1042px; }
  .card {
    position: absolute; top: 0; width: 579px; height: 1042px;
    background: linear-gradient(180deg, var(--field) 0%, var(--field-edge) 100%);
    overflow: hidden;
  }
  .card--info { left: 0; }
  .card--brand { left: 621px; }

  .streak {
    position: absolute; left: 0; right: 0; height: 2px;
    background: var(--neon);
    box-shadow: 0 0 6px var(--neon-soft);
  }
  .card--info .streak { top: 790px; right: 40px; left: 39px; }
  .card--brand .streak { top: 150px; left: 22px; right: 22px; }

  .masthead {
    position: absolute; top: 6px; left: 22px; right: 22px;
    display: flex; justify-content: space-between;
    font-family: "Bebas Neue", sans-serif; font-size: 118px; line-height: 1;
    color: var(--wordmark-faint);
  }

  .contact {
    position: absolute; left: 39px; top: 813px;
    font-family: "Open Sans", sans-serif; font-style: normal;
    font-size: 21.5px; line-height: 32.5px;
    color: var(--text);
  }
  .contact__name { font-weight: 700; color: var(--neon); }

  .disc { position: absolute; left: 180px; top: 540px; width: 336px; height: 336px; }

  .signature {
    position: absolute; left: 31px; top: 930px;
    display: flex; align-items: flex-start; gap: 14px;
  }
  .signature__name {
    font-family: "Bebas Neue", sans-serif; font-size: 72px; line-height: 1;
    letter-spacing: 15px; color: var(--neon);
  }
  .signature__dot {
    width: 22px; height: 22px; border-radius: 50%; background: var(--neon); margin-top: 6px;
  }
</style>
</head>
<body>
<main class="sheet">
  <section class="card card--info">
    <span class="streak" aria-hidden="true"></span>
    <address class="contact">
      <p class="contact__name">Dorian Elwood Marsh</p>
      <p>email - dorian@quillorb.example</p>
      <p>mobile - 555 013 2867</p>
      <p>web -</p>
      <p>quillorb.example: inventive technology applications</p>
      <p>quillorb-tv.example: innovative video advertising</p>
    </address>
  </section>

  <section class="card card--brand">
    <div class="masthead" aria-label="QUILLORB">
      <span>Q</span><span>U</span><span>I</span><span>L</span><span>L</span><span>O</span><span>R</span><span>B</span>
    </div>
    <span class="streak" aria-hidden="true"></span>
    <svg class="disc" viewBox="0 0 336 336" aria-hidden="true">
      <defs>
        <radialGradient id="discFace" cx="50%" cy="46%" r="55%">
          <stop offset="0" stop-color="var(--disc-core)"/>
          <stop offset="1" stop-color="var(--disc-edge)"/>
        </radialGradient>
        <linearGradient id="discRim" x1="0" y1="0.7" x2="1" y2="0.2">
          <stop offset="0" stop-color="#141416"/>
          <stop offset="0.7" stop-color="#2a2a2e"/>
          <stop offset="1" stop-color="var(--neon)"/>
        </linearGradient>
      </defs>
      <circle cx="168" cy="168" r="162" fill="url(#discFace)" stroke="url(#discRim)" stroke-width="4"/>
    </svg>
    <div class="signature">
      <span class="signature__name">QUILLORB</span>
      <span class="signature__dot"></span>
    </div>
  </section>
</main>
</body>
</html>
```